Banner Designs for Field Keep Ad Campaign

Harrowmere is a security consulting and services company that offers a service called FieldKeepUnit. FieldKeepUnit helps our customers secure large events by providing rapidly deployable security and communications technologies in a Field Keep vehicle, on a per event basis. We are looking for a designer to create a banner ad in three sizes for our campaign.
Target Market(s)
Our campaign is geared to the sports and entertainment industry, specifically large event venues and their security operation.
Industry/Entity Type
Security
Font styles to use
Other font styles liked:
- Raleway
Requirements
Must have
- Banner Objective
The visual and textual content of the banner should prompt the viewer to quickly identify the service offered and the information that is available to download.
Banner Design
Logo: FieldKeepUnit logo
Call to Action Button in Red: Get Details (On Right or or Upper Right)
Title in Larger Font: Take Control of you Events
Subtitle in smaller Font: Your Force Multiplier - Field Keep as a Service
Background: Photo of Field Keep interior or exterior or photo of female operator.
Font: Raleway
Banner Sizes
1 - 1200x670 pixels
2 - 1510x196 pixels
3 - 1200x628 pixels
Nice to have
- Follow the look and feel of the samples provided.

```html
<!DOCTYPE html>
<html lang="en">
<head>
<meta charset="utf-8">
<title>Field Keep Banner Set</title>
<link href="https://fonts.googleapis.com/css2?family=Raleway:wght@400;500;600;800;900&display=swap" rel="stylesheet">
<style>
  :root {
    --board: #5f5f5f;
    --navy: #070b14;
    --navy-mid: #0f1a2b;
    --photo-warm: #6a5a4e;
    --photo-cool: #25384f;
    --blue: #2b84d6;
    --white: #ffffff;
    --cta: #e24f33;
    --cta-shade: #b53a22;
  }
  * { box-sizing: border-box; margin: 0; padding: 0; }
  html, body { width: 1200px; height: 1199px; overflow: hidden; }
  body {
    background: var(--board);
    font-family: "Raleway", sans-serif;
    color: var(--white);
    position: relative;
  }
  .banner {
    position: absolute;
    overflow: hidden;
    background: var(--navy);
  }
  .banner__photo {
    position: absolute;
    top: 0; bottom: 0; right: 0;
    background:
      radial-gradient(ellipse at 72% 42%, rgba(170,140,118,0.85) 0%, rgba(106,90,78,0.55) 28%, rgba(37,56,79,0.25) 58%, rgba(7,11,20,0) 80%),
      linear-gradient(90deg, var(--navy) 0%, var(--navy-mid) 30%, var(--photo-cool) 60%, var(--photo-warm) 100%);
  }
  .brand { position: absolute; line-height: 1; }
  .brand__name { font-weight: 500; color: var(--white); display: block; }
  .brand__by { font-weight: 500; color: var(--white); display: block; text-align: right; }
  .headline {
    position: absolute;
    font-weight: 900;
    text-transform: uppercase;
    letter-spacing: -0.01em;
    color: var(--white);
  }
  .headline .accent { color: var(--blue); }
  .subline { position: absolute; font-weight: 500; color: var(--white); }
  .cta {
    position: absolute;
    background: var(--cta);
    color: var(--white);
    border-radius: 999px;
    box-shadow: 0 3px 0 var(--cta-shade), 3px 5px 6px rgba(0,0,0,0.55);
    display: flex; align-items: center; justify-content: center;
    font-weight: 500;
    white-space: nowrap;
  }

  /* Leaderboard */
  .banner--wide { left: 150px; top: 98px; width: 907px; height: 121px; }
  .banner--wide .banner__photo { left: 0; }
  .banner--wide .brand { left: 18px; top: 48px; }
  .banner--wide .brand__name { font-size: 19px; }
  .banner--wide .brand__by { font-size: 8px; margin-top: 3px; }
  .banner--wide .headline { left: 231px; top: 20px; font-size: 30px; line-height: 36px; white-space: nowrap; }
  .banner--wide .subline { left: 233px; top: 62px; font-size: 14.5px; line-height: 18px; }
  .banner--wide .cta { left: 466px; top: 66px; width: 94px; height: 26px; font-size: 7.5px; }

  /* Large rectangles */
  .banner--tall { left: 147px; top: 267px; width: 728px; height: 408px; }
  .banner--mid { left: 143px; top: 698px; width: 722px; height: 381px; }
  .banner--tall .banner__photo, .banner--mid .banner__photo { left: 0; }

  .banner--tall .brand { left: 33px; top: 62px; }
  .banner--tall .brand__name { font-size: 28px; }
  .banner--tall .brand__by { font-size: 12px; margin-top: 4px; }
  .banner--tall .headline { left: 54px; top: 138px; font-size: 58px; line-height: 56px; }
  .banner--tall .subline { left: 54px; top: 318px; font-size: 23px; line-height: 27px; }
  .banner--tall .cta { left: 505px; top: 322px; width: 154px; height: 44px; font-size: 13px; }

  .banner--mid .brand { left: 66px; top: 58px; }
  .banner--mid .brand__name { font-size: 26px; }
  .banner--mid .brand__by { font-size: 11px; margin-top: 4px; }
  .banner--mid .headline { left: 66px; top: 128px; font-size: 55px; line-height: 54px; }
  .banner--mid .subline { left: 66px; top: 296px; font-size: 22px; line-height: 26px; }
  .banner--mid .cta { left: 498px; top: 301px; width: 150px; height: 42px; font-size: 12.5px; }
</style>
</head>
<body>

  <section class="banner banner--wide">
    <div class="banner__photo" role="img" aria-label="Photo of a female operator wearing a headset in a dim command centre"></div>
    <div class="brand"><span class="brand__name">FieldKeepUnit</span><span class="brand__by">By Harrowmere</span></div>
    <h1 class="headline"><span class="accent">Take</span> Control <span class="accent">of your</span> Events</h1>
    <p class="subline">Your Force Multiplier<br>Field Keep as a Service</p>
    <a class="cta">Click Link for Details</a>
  </section>

  <section class="banner banner--tall">
    <div class="banner__photo" role="img" aria-label="Photo of a female operator wearing a headset in a dim command centre"></div>
    <div class="brand"><span class="brand__name">FieldKeepUnit</span><span class="brand__by">By Harrowmere</span></div>
    <h2 class="headline"><span class="accent">Take</span><br>Control <span class="accent">of</span><br><span class="accent">your</span> Events</h2>
    <p class="subline">Your Force Multiplier<br>Field Keep as a Service</p>
    <a class="cta">Click Link for Details</a>
  </section>

  <section class="banner banner--mid">
    <div class="banner__photo" role="img" aria-label="Photo of a female operator wearing a headset in a dim command centre"></div>
    <div class="brand"><span class="brand__name">FieldKeepUnit</span><span class="brand__by">By Harrowmere</span></div>
    <h2 class="headline"><span class="accent">Take</span><br>Control <span class="accent">of</span><br><span class="accent">your</span> Events</h2>
    <p class="subline">Your Force Multiplier<br>Field Keep as a Service</p>
    <a class="cta">Click Link for Details</a>
  </section>

</body>
</html>
```